Re-Design WP Site BrightPebbles.info

Site Re-design. Also Need a Button for contact on main page. Need Great Looking products re designed. Also bonus if you can install a site SEO checker on the site.

BrightPebbles.info

```html
<!DOCTYPE html>
<html lang="en">
<head>
<meta charset="utf-8">
<title>BrightPebbles.info — Digital Innovators</title>
<link href="https://fonts.googleapis.com/css2?family=Anton&family=Montserrat:wght@400;500;600;700&display=swap" rel="stylesheet">
<style>
:root{
  --teal:#0c5a78;
  --teal-dark:#08465f;
  --ink:#1e1e1e;
  --text:#6f6f6f;
  --light:#e6e6e6;
  --footer:#2e2e2e;
  --white:#ffffff;
}
*{margin:0;padding:0;box-sizing:border-box}
html,body{width:1200px;height:3429px;overflow:hidden}
body{position:relative;font-family:'Montserrat',sans-serif;color:var(--ink);background:var(--white)}
.abs{position:absolute}
.display{font-family:'Anton',sans-serif;font-weight:400;letter-spacing:-0.5px;text-transform:uppercase}

/* header */
.site-header{position:absolute;left:0;top:0;width:1200px;height:97px;background:var(--white)}
.brand{position:absolute;left:112px;top:30px;width:210px}
.brand-dot{position:absolute;left:92px;top:-14px;width:14px;height:14px;border-radius:50%;background:var(--teal)}
.brand-name{font-size:17px;font-weight:500;color:var(--teal);letter-spacing:1px;white-space:nowrap}
.brand-tag{font-size:6.5px;color:var(--teal);margin-top:3px;white-space:nowrap}
.nav{position:absolute;top:40px;left:383px;display:flex;gap:0;font-size:14px;font-weight:500}
.nav a{color:var(--ink);text-decoration:none;margin-right:29px}
.nav a.active{color:var(--teal)}
.nav-search{position:absolute;left:790px;top:41px}
.btn-outline,.btn-solid{position:absolute;top:26px;height:45px;width:111px;border-radius:23px;font-size:14px;font-weight:700;display:flex;align-items:center;justify-content:center}
.btn-outline{left:860px;border:2px solid var(--teal);color:var(--ink)}
.btn-solid{left:977px;background:var(--teal);color:var(--white)}

/* hero */
.hero{position:absolute;left:0;top:97px;width:1200px;height:601px;
  background:linear-gradient(90deg,rgba(30,50,90,.75) 0%,rgba(40,65,110,.35) 45%,rgba(60,85,130,.2) 100%),linear-gradient(180deg,#8ea3c7 0%,#5e7aa8 45%,#3c5687 100%)}
.hero-title{position:absolute;left:112px;top:197px;font-size:38px;color:var(--white)}
.hero-text{position:absolute;left:112px;top:253px;width:418px;font-size:16.5px;line-height:25px;color:var(--white);text-align:justify;font-weight:500}
.btn-hero{position:absolute;left:112px;top:352px;width:137px;height:44px;border-radius:22px;background:var(--teal);color:var(--white);font-size:13px;font-weight:700;display:flex;align-items:center;justify-content:center}
.slide-rail{position:absolute;left:53px;top:140px;width:2px;height:300px;background:rgba(255,255,255,.45)}
.slide-label{position:absolute;font-size:9px;font-weight:700;color:var(--white);transform:rotate(90deg);transform-origin:left top;white-space:nowrap}

/* about */
.about-photo-back{position:absolute;left:112px;top:808px;width:360px;height:347px;border-radius:14px;background:linear-gradient(135deg,#cfcfcf,#7d7d7d 60%,#4a4a4a)}
.about-photo-front{position:absolute;left:200px;top:875px;width:343px;height:303px;border-radius:12px;background:linear-gradient(160deg,#a9bcd6,#6e8cb5 55%,#445f8a)}
.about-frame{position:absolute;left:176px;top:847px;width:326px;height:360px;border:6px solid var(--teal);border-radius:14px}
.about-title{position:absolute;left:599px;top:818px;font-size:30px;color:var(--ink)}
.about-text{position:absolute;left:599px;top:882px;width:489px;font-size:14.5px;line-height:25.8px;color:var(--text);text-align:justify}
.btn-read{position:absolute;left:599px;top:1147px;width:132px;height:45px;border-radius:23px;background:var(--teal);color:var(--white);font-size:13px;font-weight:700;display:flex;align-items:center;justify-content:center}

/* solutions */
.tile{position:absolute;width:295px;height:295px;overflow:hidden}
.tile-label{position:absolute;left:0;right:0;bottom:32px;text-align:center;color:var(--white);font-size:17px;font-weight:600}
.tile-heading{display:flex;align-items:center;justify-content:center;background:var(--light);font-size:46px}

/* blog */
.blog-title{position:absolute;left:0;width:1200px;top:2008px;text-align:center;font-size:42px}
.card{position:absolute;top:2088px;width:307px;height:412px;background:var(--white);border-radius:6px;box-shadow:0 2px 14px rgba(0,0,0,.12)}
.card-img{position:absolute;left:6px;top:6px;width:295px;height:212px;border-radius:4px}
.card-date{position:absolute;top:235px;width:100%;text-align:center;font-size:12.5px;color:var(--text)}
.card-date svg{vertical-align:-2px;margin-right:5px}
.card-title{position:absolute;top:264px;width:100%;text-align:center;font-size:18px;font-weight:500}
.card-text{position:absolute;top:296px;left:12px;right:12px;text-align:center;font-size:12.5px;line-height:21.5px;color:var(--text)}
.card-more{position:absolute;top:374px;width:100%;text-align:center;font-size:14px;font-weight:700;color:var(--teal)}
.card-more svg{vertical-align:-2px;margin-left:5px}

/* contact */
.contact{position:absolute;left:0;top:2618px;width:1200px;height:473px;background:linear-gradient(180deg,rgba(12,90,120,.92),rgba(12,90,120,.85)),linear-gradient(90deg,#0a3b52,#17708f 50%,#0a3b52)}
.contact-title{position:absolute;left:0;width:1200px;top:58px;text-align:center;color:var(--white);font-size:40px}
.field{position:absolute;background:var(--white);border-radius:25px;font-size:13px;color:#888;padding-left:22px;display:flex;align-items:center}
.field-input{left:197px;width:391px;height:50px}
.field-msg{left:608px;top:149px;width:395px;height:180px;border-radius:22px;align-items:flex-start;padding-top:20px}
.btn-send{position:absolute;left:514px;top:356px;width:172px;height:51px;border-radius:26px;background:var(--white);color:var(--ink);font-size:16px;font-weight:500;display:flex;align-items:center;justify-content:center}

/* footer */
.footer{position:absolute;left:0;top:3091px;width:1200px;height:338px;background:var(--footer);color:var(--white)}
.foot-brand{position:absolute;left:112px;top:137px}
.foot-brand .brand-name{color:var(--white)}
.foot-brand .brand-tag{color:#cfcfcf}
.foot-brand .brand-dot{background:var(--white)}
.foot-head{position:absolute;top:60px;font-size:16.5px;font-weight:600}
.foot-item{position:absolute;font-size:12.5px;line-height:17px}
.foot-item b{display:block;font-size:11.5px;font-weight:600}
.foot-links{position:absolute;left:678px;top:105px;font-size:13px;line-height:32.5px}
.foot-note{position:absolute;left:842px;top:103px;width:250px;font-size:12.5px;line-height:23px}
.btn-foot{position:absolute;left:842px;top:185px;width:198px;height:45px;border-radius:23px;background:var(--teal);font-size:13px;font-weight:700;display:flex;align-items:center;justify-content:center}
.foot-rule{position:absolute;left:112px;top:279px;width:976px;height:1px;background:#6a6a6a}
.copyright{position:absolute;left:112px;top:300px;font-size:12.5px}
.social{position:absolute;top:293px;width:28px;height:28px;border-radius:50%;background:var(--white)}
</style>
</head>
<body>

<header class="site-header">
  <div class="brand">
    <span class="brand-dot"></span>
    <div class="brand-name">BRIGHTPEBBLES.info</div>
    <div class="brand-tag">Cutting Edge Business Services to Help You Reach Further</div>
  </div>
  <nav class="nav">
    <a class="active">HOME</a><a>SHOP</a><a>SOLUTIONS</a><a>BLOG</a><a>CONTACT</a>
  </nav>
  <svg class="nav-search" width="14" height="14" viewBox="0 0 14 14"><circle cx="5.5" cy="5.5" r="4.2" fill="none" stroke="#1e1e1e" stroke-width="2"/><line x1="8.6" y1="8.6" x2="12.5" y2="12.5" stroke="#1e1e1e" stroke-width="2.2"/></svg>
  <div class="btn-outline">SIGN UP</div>
  <div class="btn-solid">LOGIN</div>
</header>

<section class="hero" role="img" aria-label="Business team meeting around a table in a bright office, overlaid with blue digital patterns">
  <div class="slide-rail"></div>
  <span class="slide-label" style="left:58px;top:150px">SLIDE</span>
  <svg class="abs" style="left:33px;top:195px" width="42" height="42" viewBox="0 0 42 42"><circle cx="21" cy="21" r="20" fill="#fff"/><path d="M17 14 L28 21 L17 28Z" fill="#0c5a78"/></svg>
  <svg class="abs" style="left:44px;top:347px" width="20" height="20" viewBox="0 0 20 20"><circle cx="10" cy="10" r="8" fill="none" stroke="#fff" stroke-width="1.5"/><circle cx="10" cy="10" r="2.5" fill="#fff"/></svg>
  <span class="slide-label" style="left:58px;top:385px">TAP TO PLAY</span>
  <h1 class="hero-title display">We Are Digital Innovators</h1>
  <p class="hero-text">We're a studio of creators inventing unique and effective IT applications providing solutions that solve real world problems.</p>
  <div class="btn-hero">CONTACT US</div>
</section>

<section class="about">
  <div class="about-photo-back" role="img" aria-label="Close-up of a wristwatch in black and white"></div>
  <div class="about-photo-front" role="img" aria-label="Hand holding a tablet with a SaaS cloud diagram"></div>
  <div class="about-frame"></div>
  <h2 class="about-title display">About Bright Pebbles</h2>
  <p class="about-text">All-In-One Business Software Solution To Dominate Local Businesses. Best Small Business CRM Software online. The Best SaaS business software platform. BrightPebbles.info is a saas company that provides software solutions to businesses of all sizes. We offer a variety of saas software products that can help your business improve its productivity and efficiency. Our saas business products are easy to use and our team is always available to help you get the most out of them. Use our free trial to learn more about our software company how we can help your business grow.</p>
  <div class="btn-read">READ MORE</div>
</section>

<section class="solutions">
  <div class="tile tile-heading display" style="left:4px;top:1329px">Solutions</div>
  <div class="tile" style="left:303px;top:1329px;background:linear-gradient(150deg,#b9a27a,#5a6b7c 55%,#26394d)" role="img" aria-label="Laptop with advertising icons"><span class="tile-label">ADVERTISING</span></div>
  <div class="tile" style="left:602px;top:1329px;background:linear-gradient(150deg,#5c88b0,#2f5a85 55%,#1c3553)" role="img" aria-label="Hands on a phone with reaction icons"><span class="tile-label">REPUTATION</span></div>
  <div class="tile" style="left:901px;top:1329px;background:radial-gradient(circle at 55% 45%,#d98a80,#4e5c7e 45%,#1b2440)" role="img" aria-label="Digital cloud network graphic"><span class="tile-label">LISTINGS</span></div>
  <div class="tile" style="left:4px;top:1628px;background:linear-gradient(150deg,#2a4056,#4a3a35 50%,#7a6a60)" role="img" aria-label="Developer coding at a desk by a brick wall"><span class="tile-label">WEBSITE</span></div>
  <div class="tile" style="left:303px;top:1628px;background:linear-gradient(150deg,#8e9aa6,#4c5a68 55%,#242e38)" role="img" aria-label="Laptop with SEO icons"><span class="tile-label">SEO</span></div>
  <div class="tile" style="left:602px;top:1628px;background:var(--teal)">
    <svg class="abs" style="left:124px;top:100px" width="48" height="48" viewBox="0 0 48 48" fill="none" stroke="#fff" stroke-width="2"><rect x="6" y="16" width="18" height="26" rx="2"/><rect x="30" y="4" width="12" height="10" rx="2"/><rect x="12" y="4" width="12" height="10" rx="2"/><path d="M24 10h6M15 34h6M32 20l6 6-6 6"/></svg>
    <span class="tile-label" style="bottom:104px">SOCIAL MEDIA</span>
    <span class="abs" style="left:124px;top:193px;width:48px;height:2px;background:#fff"></span>
  </div>
  <div class="tile" style="left:901px;top:1628px;background:linear-gradient(150deg,#d9d4cc,#8f8a84 55%,#4c4844)" role="img" aria-label="Team celebrating in an office"><span class="tile-label">CONTENT &amp; EXPERIENCE</span></div>
</section>

<section class="blog">
  <h2 class="blog-title display">Recent Blog</h2>
  <article class="card" style="left:112px">
    <div class="card-img" style="background:linear-gradient(150deg,#e4e0d8,#b8ad9c 55%,#6f6658)" role="img" aria-label="Two colleagues smiling at a laptop"></div>
    <div class="card-date"><svg width="12" height="12" viewBox="0 0 12 12"><rect x="1" y="2" width="10" height="9" fill="none" stroke="#0c5a78" stroke-width="1.5"/><line x1="1" y1="5" x2="11" y2="5" stroke="#0c5a78" stroke-width="1.5"/></svg>July 29, 2022</div>
    <h3 class="card-title">Cost of Search SEO Report</h3>
    <p class="card-text">Cost of Search SEO Report – Appleton, WI – Chiropractor &amp; Dentist Local keywords price &amp; SEO search volume report</p>
    <div class="card-more">READ MORE<svg width="14" height="14" viewBox="0 0 14 14"><circle cx="7" cy="7" r="6.5" fill="#0c5a78"/><path d="M5.5 4l3 3-3 3" fill="none" stroke="#fff" stroke-width="1.6"/></svg></div>
  </article>
  <article class="card" style="left:446px">
    <div class="card-img" style="background:linear-gradient(150deg,#eef0ee,#9fa6a2 55%,#3f4547)" role="img" aria-label="Team meeting in a glass-walled office"></div>
    <div class="card-date"><svg width="12" height="12" viewBox="0 0 12 12"><rect x="1" y="2" width="10" height="9" fill="none" stroke="#0c5a78" stroke-width="1.5"/><line x1="1" y1="5" x2="11" y2="5" stroke="#0c5a78" stroke-width="1.5"/></svg>July 29, 2022</div>
    <h3 class="card-title">Cost of Search SEO Report</h3>
    <p class="card-text">Cost of Search SEO Report – Appleton, WI – Chiropractor &amp; Dentist Local keywords price &amp; SEO search volume report</p>
    <div class="card-more">READ MORE<svg width="14" height="14" viewBox="0 0 14 14"><circle cx="7" cy="7" r="6.5" fill="#0c5a78"/><path d="M5.5 4l3 3-3 3" fill="none" stroke="#fff" stroke-width="1.6"/></svg></div>
  </article>
  <article class="card" style="left:780px">
    <div class="card-img" style="background:linear-gradient(150deg,#9fc2d8,#4f7ea3 55%,#23466a)" role="img" aria-label="Hands on a laptop with digital data overlay"></div>
    <div class="card-date"><svg width="12" height="12" viewBox="0 0 12 12"><rect x="1" y="2" width="10" height="9" fill="none" stroke="#0c5a78" stroke-width="1.5"/><line x1="1" y1="5" x2="11" y2="5" stroke="#0c5a78" stroke-width="1.5"/></svg>July 29, 2022</div>
    <h3 class="card-title">Cost of Search SEO Report</h3>
    <p class="card-text">Cost of Search SEO Report – Appleton, WI – Chiropractor &amp; Dentist Local keywords price &amp; SEO search volume report</p>
    <div class="card-more">READ MORE<svg width="14" height="14" viewBox="0 0 14 14"><circle cx="7" cy="7" r="6.5" fill="#0c5a78"/><path d="M5.5 4l3 3-3 3" fill="none" stroke="#fff" stroke-width="1.6"/></svg></div>
  </article>
</section>

<section class="contact" role="img" aria-label="Blue-tinted background of computer screens">
  <h2 class="contact-title display">Get In Touch</h2>
  <div class="field field-input" style="top:149px">Your Name</div>
  <div class="field field-input" style="top:215px">Email Address</div>
  <div class="field field-input" style="top:281px">Phone Number</div>
  <div class="field field-msg">Message</div>
  <div class="btn-send">SEND MESSAGE</div>
</section>

<footer class="footer">
  <div class="foot-brand">
    <span class="brand-dot"></span>
    <div class="brand-name">BRIGHTPEBBLES.info</div>
    <div class="brand-tag">Cutting Edge Business Services to Help You Reach Further</div>
  </div>

  <div class="foot-head" style="left:363px">OUR OFFICE ADDRESS</div>
  <svg class="abs" style="left:363px;top:106px" width="12" height="12" viewBox="0 0 12 12"><path d="M2 1l3 0 1 3-1.5 1a7 7 0 0 0 3 3L9 6.5l3 1v3c-5 1-11-5-10-10z" fill="#0c5a78"/></svg>
  <div class="foot-item" style="left:396px;top:104px"><b>Phone</b>123 456 7890</div>
  <svg class="abs" style="left:363px;top:154px" width="13" height="10" viewBox="0 0 13 10"><rect width="13" height="10" fill="#0c5a78"/><path d="M0 0l6.5 5L13 0" fill="none" stroke="#2e2e2e" stroke-width="1.2"/></svg>
  <div class="foot-item" style="left:396px;top:152px"><b>Email</b>info@brightpebbles.info</div>
  <svg class="abs" style="left:364px;top:200px" width="10" height="13" viewBox="0 0 10 13"><path d="M5 13C1 8 0 6 0 5a5 5 0 0 1 10 0c0 1-1 3-5 8z" fill="#0c5a78"/><circle cx="5" cy="5" r="1.8" fill="#2e2e2e"/></svg>
  <div class="foot-item" style="left:396px;top:199px"><b>Location</b>Bright Pebbles<br>504 Lorem ipsum dolor sit amet,</div>

  <div class="foot-head" style="left:671px">COMPANY</div>
  <div class="foot-links">Home<br>Shop<br>Solution<br>Blog<br>Contact Us</div>

  <div class="foot-head" style="left:842px">STIL HAVE QUESTIOS?</div>
  <p class="foot-note">Contact us using this form. A representative will answer your questions as soon as possible.</p>
  <div class="btn-foot">CONTACT US TODAY</div>

  <div class="foot-rule"></div>
  <div class="copyright">© 2022 Bright Pebbles &nbsp;| All Rights Reserved</div>
  <span class="social" style="left:983px"></span>
  <span class="social" style="left:1021px;background:var(--teal)"></span>
  <span class="social" style="left:1059px"></span>
</footer>

</body>
</html>
```